need professional, precise design for a website

I will start with a homepage design and if we pick your design, we'll have you design up to 6 more interior pages (we'll pay extra for these of course). We need a homepage design for a reserve study company based in Idaho, covering the northwest region. The company is called copper ridge reserve study. Their current site is at https://www.copperridgereserves.example/ and they really like this site for inspiration https://www.fundplannerhub.example/ but they would like an original design, just more modern and fresh like the sample site. I have logo files I will attach. They want something that looks financial and has a feel of accuity. Their main call to action will be to have someone fill in a contact form or call them on the phone. They will have a sample study that someone can download as on the fundplannerhub site. You can use copy from their current site.

```html
<!DOCTYPE html>
<html lang="en">
<head>
<meta charset="utf-8">
<title>Copper Ridge Reserves – Association Analytics</title>
<link rel="stylesheet" href="https://fonts.googleapis.com/css2?family=Cinzel:wght@400;500&family=Open+Sans:wght@400;600;700&display=swap">
<style>
:root{
  --navy:#231f5c;
  --navy-deep:#1c1850;
  --ink:#222;
  --muted:#777;
  --white:#fff;
  --band:#6a6a6a;
  --footer:#141414;
  --line:#d8d8d8;
  --icon-bg:#8a8a8a;
}
*{box-sizing:border-box;margin:0;padding:0}
html,body{width:1200px;height:3888px;overflow:hidden}
body{font-family:"Open Sans",Arial,sans-serif;color:var(--ink);background:var(--white);position:relative}
.serif{font-family:"Cinzel",Georgia,serif;font-weight:400}

/* header */
.site-header{position:absolute;top:0;left:0;width:1200px;height:122px;background:var(--white)}
.brand{position:absolute;left:117px;top:30px;display:flex;align-items:center;gap:14px}
.brand-dot{width:46px;height:46px;border-radius:50%;background:var(--navy)}
.brand-name{font-family:"Cinzel",Georgia,serif;font-size:32px;color:var(--navy);letter-spacing:.5px}
.phone{position:absolute;left:690px;top:24px;font-family:"Cinzel",Georgia,serif;font-size:19px;color:var(--ink);display:flex;align-items:center;gap:8px}
.portal{position:absolute;left:920px;top:16px;width:168px;height:44px;border:2px solid var(--navy);border-radius:22px;display:flex;align-items:center;justify-content:center;gap:6px;font-size:14px;font-weight:700;color:var(--navy)}
.main-nav{position:absolute;top:79px;left:622px;display:flex;gap:26px;font-family:"Cinzel",Georgia,serif;font-size:16px;color:var(--ink)}
.search{position:absolute;left:1066px;top:80px}

/* hero */
.hero{position:absolute;top:122px;left:0;width:1200px;height:562px;background:linear-gradient(180deg,#5f7386 0%,#8a7a5f 35%,#6a5a40 65%,#3c3a30 100%);text-align:center;color:var(--white)}
.hero-title{position:absolute;top:118px;width:100%;font-size:64px;letter-spacing:3px}
.hero-sub{position:absolute;top:222px;width:100%;font-size:26px}
.hero-cta{position:absolute;left:482px;top:295px;width:236px;height:62px;border:3px solid var(--white);border-radius:31px;display:flex;align-items:center;justify-content:center;font-weight:700;font-size:18px}
.dots{position:absolute;top:482px;left:0;width:100%;display:flex;justify-content:center;gap:6px}
.dots span{width:14px;height:14px;border-radius:50%;border:2px solid var(--white)}
.dots span.on{background:var(--white)}

/* welcome */
.welcome{position:absolute;top:684px;left:0;width:1200px;height:591px}
.welcome h1{position:absolute;left:109px;top:80px;width:490px;font-size:42px;line-height:58px;color:var(--ink);white-space:nowrap}
.welcome p{position:absolute;left:109px;width:460px;font-size:14px;line-height:24px;color:#555}
.welcome .p1{top:216px}
.welcome .p2{top:290px}
.btn-outline{display:flex;align-items:center;justify-content:center;border:3px solid var(--navy);border-radius:30px;font-weight:700;color:var(--navy)}
.welcome .read-more{position:absolute;left:109px;top:436px;width:155px;height:54px;font-size:16px}
.video{position:absolute;left:617px;top:94px;width:471px;height:308px;border:6px solid var(--white);box-shadow:0 0 0 1px var(--line);background:linear-gradient(180deg,#8fa6bf 0%,#9c8c6c 45%,#6d5a3a 100%)}
.play{position:absolute;left:50%;top:50%;width:58px;height:58px;margin:-29px 0 0 -29px;border-radius:50%;background:#111}

/* properties */
.properties{position:absolute;top:1275px;left:0;width:1200px;height:778px;background:var(--navy);color:var(--white);text-align:center}
.properties h2{position:absolute;top:88px;width:100%;font-size:42px;letter-spacing:1px}
.prop{position:absolute;width:262px;margin-left:-131px}
.prop .circ{width:124px;height:124px;border-radius:50%;background:var(--icon-bg);margin:0 auto;display:flex;align-items:center;justify-content:center}
.prop h3{margin-top:24px;font-size:20px;font-weight:600}
.prop p{margin-top:10px;font-size:14px}

/* how it works */
.how{position:absolute;top:2053px;left:0;width:1200px;height:643px;text-align:center}
.how h2{position:absolute;top:100px;width:100%;font-size:46px;color:var(--ink)}
.step{position:absolute;top:206px;width:340px;margin-left:-170px}
.step svg{display:block;margin:0 auto}
.step h3{margin-top:24px;font-size:21px;font-weight:600;line-height:36px;letter-spacing:.5px}
.step p{margin:16px auto 0;width:300px;font-size:14px;line-height:28px;color:var(--muted)}
.arrow{position:absolute;top:260px}

/* sample band */
.sample{position:absolute;top:2696px;left:0;width:1200px;height:344px;background:var(--band);text-align:center;color:var(--white)}
.sample h2{position:absolute;top:58px;width:100%;font-size:37px;font-weight:600;line-height:52px}
.sample .btn{position:absolute;left:446px;top:197px;width:308px;height:64px;border:3px solid var(--white);border-radius:32px;display:flex;align-items:center;justify-content:center;font-weight:700;font-size:16px}

/* statistics */
.stats{position:absolute;top:3040px;left:0;width:1200px;height:602px;text-align:center}
.stats h2{position:absolute;top:92px;width:100%;font-size:42px}
.stat{position:absolute;top:197px;width:299px;height:244px;border:2px solid var(--line);border-radius:30px}
.stat .num{margin-top:44px;font-size:48px;font-weight:700;color:var(--navy)}
.stat .num sup{font-size:26px;vertical-align:-14px}
.stat .lbl{margin-top:18px;font-size:20px;font-weight:600;line-height:36px}

/* footer */
.social{position:absolute;top:3613px;left:0;width:1200px;display:flex;justify-content:center;gap:14px;z-index:2}
.social span{width:52px;height:52px;border-radius:50%;background:var(--navy);border:2px solid var(--white)}
.site-footer{position:absolute;top:3642px;left:0;width:1200px;height:246px;background:var(--footer);color:var(--white);text-align:center;font-size:14px}
.contact-line{position:absolute;top:82px;width:100%;display:flex;justify-content:center;align-items:center;gap:10px}
.links{position:absolute;top:128px;width:100%;display:flex;justify-content:center;gap:14px}
.copy{position:absolute;top:170px;width:100%}
</style>
</head>
<body>

<header class="site-header">
  <div class="brand"><span class="brand-dot"></span><span class="brand-name">Copper Ridge Reserves</span></div>
  <div class="phone">
    <svg width="16" height="16" viewBox="0 0 24 24"><path d="M6.6 10.8a15 15 0 0 0 6.6 6.6l2.2-2.2c.3-.3.7-.4 1-.2 1.1.4 2.3.6 3.6.6.6 0 1 .4 1 1V20c0 .6-.4 1-1 1A17 17 0 0 1 3 4c0-.6.4-1 1-1h3.5c.6 0 1 .4 1 1 0 1.3.2 2.5.6 3.6.1.3 0 .7-.2 1z" fill="#222"/></svg>
    CALL (208) 555-0147
  </div>
  <div class="portal">
    <svg width="13" height="13" viewBox="0 0 24 24"><circle cx="12" cy="7" r="5" fill="#231f5c"/><path d="M2 23c0-6 4.5-9 10-9s10 3 10 9z" fill="#231f5c"/></svg>
    CLIENT PORTAL
  </div>
  <nav class="main-nav"><span>HOME</span><span>ABOUT</span><span>RESERVE STUDIES</span><span>CONTACT US</span></nav>
  <svg class="search" width="18" height="18" viewBox="0 0 24 24"><circle cx="10" cy="10" r="7" fill="none" stroke="#222" stroke-width="3"/><path d="M15 15l7 7" stroke="#222" stroke-width="3"/></svg>
</header>

<section class="hero" role="img" aria-label="Aerial view of a hillside residential neighbourhood at sunset">
  <h1 class="hero-title serif">ASSOCIATION ANALYTICS</h1>
  <p class="hero-sub">Your financial road map for the next 30 years!</p>
  <div class="hero-cta">REQUEST A QUOTE</div>
  <div class="dots"><span class="on"></span><span></span><span></span><span></span></div>
</section>

<section class="welcome">
  <h1 class="serif">Welcome to<br>Copper Ridge Reserve</h1>
  <p class="p1">A sound reserve plan is a constant that community boards have relied on for decades.</p>
  <p class="p2">Planning ahead is simply knowing the right points of origin and following the map that careful numbers have laid before us. We love the details! Amidst so many components and a seemingly chaotic expanse of costs and dates, there is great order.</p>
  <div class="read-more btn-outline">READ MORE</div>
  <div class="video" role="img" aria-label="Video thumbnail of a city skyline with a historic red-roofed building">
    <span class="play"></span>
    <svg style="position:absolute;left:50%;top:50%;margin:-11px 0 0 -7px" width="20" height="22" viewBox="0 0 20 22"><path d="M0 0l20 11L0 22z" fill="#fff"/></svg>
  </div>
</section>

<section class="properties">
  <h2 class="serif">We work with all types of properties</h2>
  <div class="prop" style="left:207px;top:210px"><div class="circ"><svg width="60" height="60" viewBox="0 0 60 60" fill="none" stroke="#fff" stroke-width="2.5"><path d="M8 30L30 10l22 20M14 25v27h32V25"/><rect x="25" y="36" width="10" height="16"/></svg></div><h3>Homeowners</h3><p>Nam libero tempore cum solu</p></div>
  <div class="prop" style="left:469px;top:210px"><div class="circ"><svg width="60" height="60" viewBox="0 0 60 60" fill="none" stroke="#fff" stroke-width="2.5"><path d="M8 20L30 8l22 12zM12 24h36M16 26v22M26 26v22M34 26v22M44 26v22M8 52h44"/></svg></div><h3>Associations</h3><p>Nam libero tempore cum solu</p></div>
  <div class="prop" style="left:731px;top:210px"><div class="circ"><svg width="60" height="60" viewBox="0 0 60 60" fill="none" stroke="#fff" stroke-width="2.5"><path d="M10 52V26h14v26M24 52V12l24 8v32M6 52h48M30 22h12M30 30h12M30 38h12"/></svg></div><h3>Commercial Property</h3><p>Nam libero tempore cum solu</p></div>
  <div class="prop" style="left:993px;top:210px"><div class="circ"><svg width="60" height="60" viewBox="0 0 60 60" fill="none" stroke="#fff" stroke-width="2.5"><rect x="14" y="10" width="32" height="42"/><path d="M20 18h6M34 18h6M20 28h6M34 28h6M20 38h6M34 38h6M8 52h44"/></svg></div><h3>Condominiums</h3><p>Nam libero tempore cum solu</p></div>
  <div class="prop" style="left:207px;top:477px"><div class="circ"><svg width="60" height="60" viewBox="0 0 60 60" fill="none" stroke="#fff" stroke-width="2.5"><rect x="10" y="14" width="40" height="34" rx="3"/><path d="M10 22h40M18 10v8M42 10v8"/><circle cx="36" cy="38" r="5"/></svg></div><h3>Time Shares</h3><p>Nam libero tempore cum solu</p></div>
  <div class="prop" style="left:469px;top:477px"><div class="circ"><svg width="60" height="60" viewBox="0 0 60 60" fill="none" stroke="#fff" stroke-width="2.5"><path d="M12 52V24l18-14 18 14v28M6 52h48M22 30h6M32 30h6M22 40h6M32 40h6"/></svg></div><h3>Common Area Assets</h3><p>Nam libero tempore cum solu</p></div>
  <div class="prop" style="left:731px;top:477px"><div class="circ"><svg width="60" height="60" viewBox="0 0 60 60" fill="none" stroke="#fff" stroke-width="2.5"><rect x="16" y="8" width="28" height="44"/><path d="M22 16h5M33 16h5M22 25h5M33 25h5M22 34h5M33 34h5M27 52v-8h6v8"/></svg></div><h3>Apartments</h3><p>Nam libero tempore cum solu</p></div>
  <div class="prop" style="left:993px;top:477px"><div class="circ"><svg width="60" height="60" viewBox="0 0 60 60" fill="none" stroke="#fff" stroke-width="2.5"><path d="M30 8L18 26h6L14 40h32L36 26h6zM30 40v10M10 52h40"/></svg></div><h3>Parks</h3><p>Nam libero tempore cum solu</p></div>
</section>

<section class="how">
  <h2 class="serif">How IT Works</h2>
  <div class="step" style="left:259px">
    <svg width="100" height="120" viewBox="0 0 100 120" fill="none" stroke="#1c1850" stroke-width="5"><rect x="16" y="14" width="68" height="100" rx="4"/><rect x="36" y="6" width="28" height="14" fill="#1c1850"/><path d="M28 44l5 5 8-10M48 44h26M28 66l5 5 8-10M48 66h26M28 88l5 5 8-10M48 88h26"/></svg>
    <h3>COMPONENT<br>LIST</h3>
    <p>Nam libero tempore, cum soluta nobis est eligendi optio cumque nihil impedit quo minus id quod maxime placea</p>
  </div>
  <svg class="arrow" style="left:392px" width="72" height="28" viewBox="0 0 72 28"><path d="M4 22Q34 2 62 14" fill="none" stroke="#777" stroke-width="5"/><path d="M56 4l12 12-16 6z" fill="#777"/></svg>
  <div class="step" style="left:599px">
    <svg width="100" height="120" viewBox="0 0 100 120"><rect x="30" y="30" width="56" height="86" rx="4" fill="#1c1850"/><g fill="#fff"><rect x="38" y="40" width="40" height="14"/><rect x="38" y="62" width="10" height="10"/><rect x="53" y="62" width="10" height="10"/><rect x="68" y="62" width="10" height="10"/><rect x="38" y="78" width="10" height="10"/><rect x="53" y="78" width="10" height="10"/><rect x="68" y="78" width="10" height="10"/><rect x="38" y="94" width="10" height="10"/><rect x="53" y="94" width="10" height="10"/><rect x="68" y="94" width="10" height="10"/></g><text x="4" y="42" font-family="Open Sans,Arial,sans-serif" font-size="48" font-weight="700" fill="#1c1850">$</text></svg>
    <h3>CALCULATION OF<br>RESERVE FUND STRENGTH</h3>
    <p>Nam libero tempore, cum soluta nobis est eligendi optio cumque nihil impedit quo minus id quod maxime placea</p>
  </div>
  <svg class="arrow" style="left:736px" width="72" height="28" viewBox="0 0 72 28"><path d="M4 10Q34 30 62 16" fill="none" stroke="#777" stroke-width="5"/><path d="M54 6l14 8-14 10z" fill="#777"/></svg>
  <div class="step" style="left:938px">
    <svg width="120" height="120" viewBox="0 0 120 120" fill="none" stroke="#1c1850" stroke-width="5"><rect x="10" y="20" width="76" height="56"/><path d="M24 66V50M36 66V40M48 66V46M60 66V34M48 76v24M36 100l12-24 12 24"/><circle cx="98" cy="34" r="9" fill="#1c1850"/><path d="M90 48h16v50M98 98V70M86 50l-10 10"/></svg>
    <h3>CUSTOM<br>FUNDING PLAN</h3>
    <p>Nam libero tempore, cum soluta nobis est eligendi optio cumque nihil impedit quo minus id quod maxime placea</p>
  </div>
</section>

<section class="sample">
  <h2>Our report covers a one-year period and<br>includes a 30-year cash flow forecast</h2>
  <div class="btn">READ SAMPLE RESERVE STUDY</div>
</section>

<section class="stats">
  <h2 class="serif">Statistics</h2>
  <div class="stat" style="left:111px"><div class="num">$ 450</div><div class="lbl">Million Funding<br>Guidance Provided</div></div>
  <div class="stat" style="left:451px"><div class="num">55,000<sup>+</sup></div><div class="lbl">Reserve Studies<br>Completed</div></div>
  <div class="stat" style="left:790px"><div class="num">35</div><div class="lbl">Years<br>Experience</div></div>
</section>

<div class="social" role="img" aria-label="Social media links"><span></span><span></span><span></span><span></span></div>

<footer class="site-footer">
  <div class="contact-line">
    <svg width="12" height="16" viewBox="0 0 12 16"><path d="M6 0a6 6 0 0 0-6 6c0 4.5 6 10 6 10s6-5.5 6-10a6 6 0 0 0-6-6z" fill="#fff"/><circle cx="6" cy="6" r="2.2" fill="#141414"/></svg>
    <span>Serving Idaho, Montana, Oregon, Utah, Washington &amp; Wyoming</span><span>|</span>
    <svg width="14" height="14" viewBox="0 0 24 24"><path d="M6.6 10.8a15 15 0 0 0 6.6 6.6l2.2-2.2c.3-.3.7-.4 1-.2 1.1.4 2.3.6 3.6.6.6 0 1 .4 1 1V20c0 .6-.4 1-1 1A17 17 0 0 1 3 4c0-.6.4-1 1-1h3.5c.6 0 1 .4 1 1 0 1.3.2 2.5.6 3.6.1.3 0 .7-.2 1z" fill="#fff"/></svg>
    <span>(208) 555-0147</span><span>|</span>
    <svg width="16" height="12" viewBox="0 0 16 12"><rect width="16" height="12" fill="#fff"/><path d="M0 0l8 7 8-7" fill="none" stroke="#141414" stroke-width="1.5"/></svg>
    <span>hello@copperridgereserves.example</span>
  </div>
  <div class="links"><span>Help</span><span>|</span><span>FAQ</span><span>|</span><span>Support</span><span>|</span><span>Sitemap</span><span>|</span><span>Terms Of Use</span><span>|</span><span>Privacy Statement</span></div>
  <div class="copy">Copper Ridge Reserves © 2019 All rights reserved.</div>
</footer>

</body>
</html>
```